Coaching business needs flyer for business market

I need a flyer that I can send to HR-managers and business owners to inform them of my coaching services for organisations. We have three services: organisational- and teamcoaching, individual coaching and training programs.
I want the flyer to express calmness, solid and trustworthy coaching. As a person I am open and think out of the box.

In my logo I use a couple of colours (blue, green, orange and grey) that represent the diversity of humans. My company's name is Bramblecrest Engagement & Coaching and tag line is "Awaken your quiet river".

I do not want the design to be too busy but also not too boring. I tried making something myself. Feel free to build on that design. Or feel free to start from scratch.

```html
<!DOCTYPE html>
<html lang="nl">
<head>
<meta charset="utf-8">
<title>Bramblecrest Engagement &amp; Coaching – flyer</title>
<link href="https://fonts.googleapis.com/css2?family=Lato:wght@300;400;700;900&display=swap" rel="stylesheet">
<style>
  :root {
    --bg: #e4e4e4;
    --paper: #f4f2f0;
    --green: #8fd0b4;
    --teal: #4cc3cf;
    --orange: #ec7a2b;
    --red: #d22a36;
    --grey: #4a484b;
    --ink: #4d4d4f;
    --white: #ffffff;
  }
  * { box-sizing: border-box; margin: 0; padding: 0; }
  html, body { width: 1200px; height: 900px; overflow: hidden; }
  body {
    background: var(--bg);
    font-family: "Lato", Arial, sans-serif;
    display: flex; align-items: center; justify-content: center;
  }
  .flyer {
    position: relative;
    width: 600px; height: 850px;
    background: var(--paper);
    overflow: hidden;
    box-shadow: 0 6px 24px rgba(0,0,0,.18);
  }
  .block { position: absolute; color: var(--white); }
  .photo { position: absolute; }

  .portrait {
    left: 0; top: 0; width: 280px; height: 580px;
    background: linear-gradient(160deg, #2b3bb4 0%, #3346c2 45%, #6b5a52 75%, #c9b7a8 100%);
  }
  .intro {
    left: 235px; top: 0; width: 365px; height: 300px;
    background: var(--green);
    padding: 30px 26px 0 34px;
  }
  .intro-pointer { position: absolute; left: 235px; top: 299px; }
  .intro h1 {
    font-weight: 900; font-size: 19px; letter-spacing: .3px;
    text-transform: uppercase; margin-bottom: 6px;
  }
  .intro p { font-size: 10.5px; line-height: 1.45; font-weight: 400; margin-bottom: 10px; }

  .service { padding: 10px 10px 12px; font-size: 9.5px; line-height: 1.35; }
  .service .photo { position: relative; width: 100%; height: 100px; margin-bottom: 9px; }
  .service h2 { font-size: 10px; font-weight: 700; line-height: 1.3; margin-bottom: 7px; }
  .service ul { list-style: none; }
  .service li { position: relative; padding-left: 10px; margin-bottom: 5px; font-weight: 400; }
  .service li:last-child { margin-bottom: 0; }
  .service li::before { content: "•"; position: absolute; left: 0; }

  .training { left: 410px; top: 300px; width: 190px; background: var(--orange); }
  .training .photo { height: 110px; background: linear-gradient(135deg, #1c1f3e, #3a3f7a 60%, #6a5c8a); }
  .individual { left: 212px; bottom: 130px; width: 175px; background: var(--teal); }
  .individual .photo { background: linear-gradient(135deg, #c9a76a, #7a6a5a 55%, #9fb4d6); }
  .team { left: 30px; bottom: 82px; width: 175px; background: var(--red); }
  .team .photo { height: 90px; background: linear-gradient(135deg, #b59a84, #7b6a66 55%, #d8c4b6); }

  .methods {
    left: 0; top: 775px; width: 390px; height: 75px;
    background: var(--grey);
    padding: 9px 14px 0 22px;
    font-size: 9px; line-height: 1.3;
  }
  .methods h3 { font-size: 9.5px; font-weight: 700; margin-bottom: 3px; }
  .methods ul { list-style: none; }
  .methods li::before { content: "• "; }

  .brand {
    position: absolute; left: 390px; top: 640px; width: 210px; height: 210px;
    background: var(--white);
    display: flex; align-items: center; justify-content: center; gap: 10px;
    color: var(--ink);
  }
  .brand-dot { width: 30px; height: 30px; border-radius: 50%; background: var(--grey); flex: none; }
  .brand-name { font-size: 15px; font-weight: 300; line-height: 1.2; }
</style>
</head>
<body>
<main class="flyer">
  <div class="photo portrait" role="img" aria-label="Portretfoto van de coach, lachend, tegen een blauwe achtergrond"></div>

  <section class="block intro">
    <h1>Anjali Verhoeven</h1>
    <p>is trainer en coach. Ze heeft ruime ervaring met veranderingstrajecten binnen organisaties. Mensen omschrijven haar als ‘betrokken, warm, stevig en kordaat’. Het is haar passie om organisaties, teams en mensen te helpen groeien. Zij helpt weerstand te overwinnen en draagt bij aan groei in zelfvertrouwen. Haar trainingen en coaching zijn erop gericht om snel inzichtelijk te krijgen welke stappen men moet zetten om verder te komen.</p>
    <p>Ze gelooft de veranderkracht van de mensen waar ze mee werkt. Ze is er om steun en richting te bieden en laat hen zelf aan het roer.</p>
  </section>
  <svg class="intro-pointer" width="40" height="45" viewBox="0 0 40 45" aria-hidden="true">
    <polygon points="0,0 40,0 8,45" fill="var(--green)"/>
  </svg>

  <section class="block service training">
    <div class="photo" role="img" aria-label="Foto van een zaal met publiek tijdens een workshop"></div>
    <h2>Ontwikkeling &amp; Borging van kennis en vakmanschap door LEERGANGEN, TRAININGEN &amp; WORKSHOPS op MAAT:</h2>
    <ul>
      <li>Leiderschap</li>
      <li>Communicatie</li>
      <li>Leren kijken met ‘systemische bril’ voor professionals</li>
      <li>Conflicthantering</li>
    </ul>
  </section>

  <section class="block service individual">
    <div class="photo" role="img" aria-label="Foto van een individueel coachgesprek"></div>
    <h2>Duurzame Inzetbaarheid door INDIVIDUELE Coaching:</h2>
    <ul>
      <li>Wens je medewerkers die hun talent ten volste benutten?</li>
      <li>Verlang je meer authentieke leiderschap bij je collega’s?</li>
      <li>Wil je de mensen vooruit helpen in hun loopbaan?</li>
      <li>Zoek je steun voor medewerkers met burn-out of re-integratie?</li>
      <li>Heb je hulp nodig bij outplacement trajecten?</li>
    </ul>
  </section>

  <section class="block service team">
    <div class="photo" role="img" aria-label="Foto van een team tijdens een teamcoachingsessie"></div>
    <h2>Een organisatie waar medewerkers gemotiveerd zijn, samenwerken, communiceren zonder gedoe door ORGANISATIE- of TEAM coaching:</h2>
    <ul>
      <li>Heb je zorgen voor of na een fusie of verandering?</li>
      <li>Wil je missie, visie &amp; strategie ontwikkelen of wijzigen?</li>
      <li>Wens je de cultuur veranderen of verder ontwikkelen?</li>
      <li>Beoog je de samenwerking bevorderen of verbeteren?</li>
    </ul>
  </section>

  <section class="block methods">
    <h3>Gedegen resultaat en kwaliteit door bewezen ‘best practices’</h3>
    <ul>
      <li>Neuro Linguïstisch Programmeren (NLP)</li>
      <li>Transactionele Analyse</li>
      <li>Systemisch Werken: Organisatie-, Familie- en Traumaopstellingen</li>
      <li>Somatic Experience, Ademwerk en Lichaamswerk</li>
    </ul>
  </section>

  <footer class="brand">
    <span class="brand-dot" aria-hidden="true"></span>
    <span class="brand-name">Bramblecrest<br>Engagement &amp; Coaching</span>
  </footer>
</main>
</body>
</html>
```